Stationery & business cards for nonprofit
WELL Wells of kindness beyond measure
Stationery & business cards for nonprofit - Religion and Spirituality
Creative Brief
Use same font as used in my logo
Ruth Pelling
President
481 Orchard Lane Birmingham, AL 35187
ruth@wellkb.org
www.wellkb.org
We are open to ideas and suggestions using our logo, this is a nonprofit that supports an orphanage and assists widows in Africa, as shown in the earth tone in the logo. Logo information: Font: Desire (manipulated), Swiss Condensed, Times Roman Color: Pantone 1395, Pantone 7407, Pantone 364 Our website is currently under development, but you can see pictures, etc to get a feel for our nonprofit by going to www.wellkb.org
We are thinking to put just the logo on the back of the card with the name (wells of kindness beyond measure) and the verse listed - I John 3:16-18
mirabelcostow mirabelcostow
AI and EPS file formats have been uploaded for use as needed.

```html
<!DOCTYPE html>
<html lang="en">
<head>
<meta charset="utf-8">
<title>WELL business card</title>
<link href="https://fonts.googleapis.com/css2?family=Open+Sans:wght@400;600;700&display=swap" rel="stylesheet">
<style>
  :root {
    --backdrop: #d9d9d9;
    --card-white: #ffffff;
    --card-black: #141414;
    --gold: #b8892a;
    --gold-light: #d9ad4c;
    --green: #3f7a26;
    --ink: #222222;
    --muted: #555555;
  }
  * { margin: 0; padding: 0; box-sizing: border-box; }
  html, body { width: 1200px; height: 878px; overflow: hidden; }
  body {
    background: var(--backdrop);
    font-family: "Open Sans", Arial, sans-serif;
    position: relative;
  }
  .card {
    position: absolute;
    width: 560px;
    height: 320px;
    overflow: hidden;
    box-shadow: 0 6px 18px rgba(0,0,0,0.18);
  }
  .card-back {
    left: 580px; top: 110px;
    background: var(--card-black);
    display: flex; align-items: center; justify-content: center;
  }
  .card-front {
    left: 60px; top: 450px;
    background: var(--card-white);
  }
  .brand { text-align: center; }
  .brand-name {
    font-weight: 700;
    font-size: 64px;
    letter-spacing: 2px;
    line-height: 1;
    color: var(--gold-light);
    display: flex; align-items: center; justify-content: center; gap: 12px;
  }
  .brand-dot {
    width: 16px; height: 16px; border-radius: 50%;
    background: var(--gold-light);
  }
  .brand-tagline {
    margin-top: 6px;
    font-weight: 600;
    font-size: 12px;
    color: var(--gold-light);
  }
  .card-front .brand {
    position: absolute; left: 40px; top: 48px; width: 230px;
  }
  .card-front .brand-name { color: var(--green); font-size: 56px; }
  .card-front .brand-dot { background: var(--green); }
  .card-front .brand-tagline { color: var(--green); font-size: 11px; }
  .contact {
    position: absolute; left: 320px; top: 70px;
    color: var(--ink);
  }
  .contact-name { font-weight: 700; font-size: 19px; }
  .contact-role { font-size: 12px; color: var(--muted); margin-bottom: 12px; }
  .contact-line {
    display: flex; align-items: center; gap: 8px;
    font-size: 12px; line-height: 18px; color: var(--ink);
  }
  .contact-line svg { width: 11px; height: 11px; flex: none; fill: var(--ink); }
  .address { font-size: 12px; line-height: 16px; margin-bottom: 4px; }
  .swoosh { position: absolute; left: 0; bottom: 0; width: 560px; height: 120px; }
  .footer-url {
    position: absolute; left: 70px; bottom: 24px;
    font-size: 12px; letter-spacing: 1px; color: #fff;
  }
</style>
</head>
<body>

  <section class="card card-back" aria-label="Card back">
    <div class="brand">
      <div class="brand-name"><span class="brand-dot"></span>WELL</div>
      <div class="brand-tagline">Wells of kindness beyond measure</div>
    </div>
  </section>

  <section class="card card-front" aria-label="Card front">
    <div class="brand">
      <div class="brand-name"><span class="brand-dot"></span>WELL</div>
      <div class="brand-tagline">Wells of kindness beyond measure</div>
    </div>

    <div class="contact">
      <div class="contact-name">Ruth Pelling</div>
      <div class="contact-role">President</div>
      <div class="address">481 Orchard Lane<br>Birmingham, AL 35187</div>
      <div class="contact-line">
        <svg viewBox="0 0 24 24"><path d="M6.6 10.8a15 15 0 0 0 6.6 6.6l2.2-2.2a1 1 0 0 1 1-.25 11.4 11.4 0 0 0 3.6.57 1 1 0 0 1 1 1V20a1 1 0 0 1-1 1A17 17 0 0 1 3 4a1 1 0 0 1 1-1h3.5a1 1 0 0 1 1 1c0 1.25.2 2.45.57 3.57a1 1 0 0 1-.25 1z"/></svg>
        123 456 7890
      </div>
      <div class="contact-line">
        <svg viewBox="0 0 24 24"><rect x="6" y="2" width="12" height="20" rx="2"/></svg>
        123 456 7890
      </div>
      <div class="contact-line">
        <svg viewBox="0 0 24 24"><rect x="2" y="7" width="20" height="12" rx="1"/><rect x="6" y="3" width="12" height="5"/></svg>
        123 456 7890
      </div>
      <div class="contact-line">
        <svg viewBox="0 0 24 24"><path d="M2 5h20v14H2z M2 5l10 8 10-8" fill="none" stroke="#222" stroke-width="2"/></svg>
        ruth@wellkb.org
      </div>
      <div class="contact-line">
        <svg viewBox="0 0 24 24"><circle cx="12" cy="12" r="10"/></svg>
        www.wellkb.org
      </div>
    </div>

    <svg class="swoosh" viewBox="0 0 560 120" preserveAspectRatio="none">
      <defs>
        <linearGradient id="goldBand" x1="0" y1="0" x2="1" y2="0">
          <stop offset="0" stop-color="#9c7220"/>
          <stop offset="0.5" stop-color="#d9ad4c"/>
          <stop offset="1" stop-color="#a97c24"/>
        </linearGradient>
      </defs>
      <path d="M0 20 C180 40 380 70 560 110 L560 120 L0 120 Z" fill="url(#goldBand)"/>
      <path d="M0 10 C180 28 380 58 560 98" fill="none" stroke="var(--green)" stroke-width="6"/>
    </svg>
    <div class="footer-url">www.wellkb.org</div>
  </section>

</body>
</html>
```